New Business Card for Casual Beachfront Cafe

Quirky Beachfront Cafe at Moana, South Australia needs a DOUBLE SIDED business card to print on PrintHarbor.

Target Market(s)

Business Cards sit on the counter for Guests to take with them. Please view our website www.saltreefcafe.com.au to get a feel for the Cafe. You may also view our Instagram at @saltreefcafe

Industry/Entity Type

Cafe / Restaurant

Contact Information for Business Card

Information equivalent to: Breakfast, Lunch, Dinner, Coffee, Takeaway / 117 Parade Tidewater Bay 0917 / Menu & Opening Hours: www.saltreefcafe.com.au / ph (08) 8461 9273

Requirements
Must have
• Information equivalent to: Breakfast, Lunch, Dinner, Coffee, Takeaway / 117 Parade Tidewater Bay 0917 / Menu & Opening Hours: www.saltreefcafe.com.au / ph (08) 8461 9273
Nice to have
• Potentially some of our trademark colours (Cafe can be searched via Seekly)
Should not have
• Must NOT have image of the building. May have the logo provided on one side but not necessarily, depending on how you wish to design the card

```html
<!DOCTYPE html>
<html lang="en">
<head>
<meta charset="utf-8">
<title>Salt Reef Cafe – Business Card</title>
<link rel="stylesheet" href="https://fonts.googleapis.com/css2?family=Montserrat:wght@400;700;800&family=Oswald:wght@500;600;700&display=swap">
<style>
  :root {
    --navy: #134480;
    --navy-light: #2a5a92;
    --yellow: #ffff00;
    --rust: #b5561b;
    --white: #ffffff;
    --peach: #efdccf;
    --backdrop: #d9dbe0;
  }
  * { box-sizing: border-box; margin: 0; padding: 0; }
  html, body { width: 1200px; height: 1015px; overflow: hidden; }
  body {
    background: var(--backdrop);
    position: relative;
    font-family: "Montserrat", sans-serif;
  }
  .card {
    position: absolute;
    left: 250px;
    width: 700px;
    height: 400px;
    overflow: hidden;
    box-shadow: 0 8px 24px rgba(0,0,0,.18);
  }

  /* ---------- Hours side ---------- */
  .card--hours { top: 50px; background: var(--navy); }
  .hours-ornament {
    position: absolute; left: -40px; top: 60px;
    width: 300px; height: 260px;
    border-radius: 50% 40% 55% 45%;
    background: var(--navy-light);
    opacity: .7;
  }
  .hours-title {
    position: absolute; top: 42px; left: 0; right: 0;
    text-align: center;
    color: var(--yellow);
    font-weight: 800; font-size: 24px; letter-spacing: .5px;
  }
  .rule {
    position: absolute; height: 1px; width: 140px;
    background: var(--yellow); left: 280px;
  }
  .rule--top { top: 80px; }
  .rule--bottom { top: 290px; }
  .day-block {
    position: absolute; display: grid; grid-template-columns: 60px auto;
    row-gap: 4px; font-size: 17px; line-height: 1.25; color: var(--white);
  }
  .day-block b { color: var(--yellow); font-weight: 800; }
  .hours-closed { left: 60px; top: 190px; }
  .hours-week { left: 270px; top: 110px; }
  .hours-weekend { left: 470px; top: 110px; grid-template-columns: 48px auto; }
  .services {
    position: absolute; left: 0; right: 0; bottom: 0; height: 82px;
    background: var(--yellow);
    display: flex; align-items: center; justify-content: center; gap: 14px;
    padding: 0 24px;
    font-family: "Oswald", sans-serif; font-weight: 600;
    font-size: 26px; color: var(--navy); letter-spacing: .3px;
  }
  .services .dot { width: 10px; height: 10px; border-radius: 50%; background: var(--rust); flex: none; }

  /* ---------- Contact side ---------- */
  .card--contact { top: 555px; background: var(--white); }
  .brand-panel {
    position: absolute; left: 0; top: 0; bottom: 0; width: 250px;
    background: var(--navy);
    display: flex; flex-direction: column; justify-content: center; align-items: center;
  }
  .brand-name {
    font-family: "Oswald", sans-serif; font-weight: 700;
    color: var(--yellow); font-size: 50px; line-height: 1.05;
    text-align: center; text-transform: uppercase;
  }
  .contact-ornament {
    position: absolute; right: -30px; top: 20px;
    width: 260px; height: 260px;
    border-radius: 55% 45% 50% 50%;
    background: var(--peach);
  }
  .contact-list {
    position: absolute; left: 290px; right: 24px; top: 0; bottom: 0;
    display: flex; flex-direction: column; justify-content: center; gap: 48px; list-style: none;
  }
  .contact-item {
    display: flex; align-items: center; gap: 16px;
    font-family: "Oswald", sans-serif; font-weight: 600; font-size: 24px;
    color: var(--navy); position: relative; white-space: nowrap;
  }
  .contact-icon {
    width: 48px; height: 42px; flex: none;
    background: var(--yellow); border: 4px solid var(--rust);
    display: flex; align-items: center; justify-content: center;
  }
  .contact-icon svg { width: 22px; height: 22px; fill: none; stroke: var(--navy); stroke-width: 2.4; }
</style>
</head>
<body>

<section class="card card--hours" aria-label="Opening hours side">
  <div class="hours-ornament" role="img" aria-label="Faint petal ornament"></div>
  <h2 class="hours-title">OPENING HOURS</h2>
  <div class="rule rule--top"></div>

  <div class="day-block hours-closed">
    <b>Mon</b><span>Closed</span>
    <b>Tues</b><span>Closed</span>
  </div>
  <div class="day-block hours-week">
    <b>Wed</b><span>9am-2pm<br>5pm-8pm</span>
    <b>Thur</b><span>9am-2pm<br>5pm-8pm</span>
    <b>Fri</b><span>9am-2pm<br>5pm-8pm</span>
  </div>
  <div class="day-block hours-weekend">
    <b>Sat</b><span>8:30am-8pm</span>
    <b>Sun</b><span>8:30am-8pm</span>
  </div>

  <div class="rule rule--bottom"></div>

  <div class="services">
    <span>BREAKFAST</span><i class="dot"></i>
    <span>LUNCH</span><i class="dot"></i>
    <span>DINNER</span><i class="dot"></i>
    <span>COFFEE</span><i class="dot"></i>
    <span>TAKEAWAY</span>
  </div>
</section>

<section class="card card--contact" aria-label="Contact side">
  <div class="brand-panel">
    <p class="brand-name">Salt Reef<br>Cafe</p>
  </div>
  <div class="contact-ornament" role="img" aria-label="Soft peach petal ornament"></div>
  <ul class="contact-list">
    <li class="contact-item">
      <span class="contact-icon"><svg viewBox="0 0 24 24"><path d="M12 22s7-7 7-12a7 7 0 0 0-14 0c0 5 7 12 7 12z"/><circle cx="12" cy="10" r="2.5"/></svg></span>
      117 PARADE TIDEWATER BAY 0917
    </li>
    <li class="contact-item">
      <span class="contact-icon"><svg viewBox="0 0 24 24"><path d="M5 3h4l2 5-2.5 1.5a11 11 0 0 0 6 6L16 13l5 2v4a2 2 0 0 1-2 2A17 17 0 0 1 3 5a2 2 0 0 1 2-2z"/></svg></span>
      (08) 8461 9273
    </li>
    <li class="contact-item">
      <span class="contact-icon"><svg viewBox="0 0 24 24"><circle cx="12" cy="12" r="9"/><path d="M3 12h18M12 3c3 3 3 15 0 18M12 3c-3 3-3 15 0 18"/></svg></span>
      WWW.SALTREEFCAFE.COM.AU
    </li>
  </ul>
</section>

</body>
</html>
```